Flyer Design

MALLOWBYS, fish & Chips . 17 Fennick Lane, Hollowmere KT4 7RD, TEL; 0208 6142937
This is a existing business of Fish and Chips, would like to use picture of fish & Chips and the menu on the other side

Industry/Entity Type

Business

```html
<!DOCTYPE html>
<html lang="en">
<head>
<meta charset="utf-8">
<title>Mallowbys Fish &amp; Chips – Flyer</title>
<link rel="stylesheet" href="https://fonts.googleapis.com/css2?family=Arimo:wght@700&family=Lora:ital,wght@1,700&family=Open+Sans:wght@600&display=swap">
<style>
  :root{
    --navy:#27295f;
    --red:#e61e2a;
    --yellow:#f2ea2a;
    --white:#ffffff;
    --page:#ece9e4;
    --crisp:#d9a24a;
    --crisp-light:#f1d9a8;
    --chip:#efe2b8;
  }
  *{margin:0;padding:0;box-sizing:border-box}
  html,body{width:1200px;height:1000px;overflow:hidden;background:var(--page)}
  .canvas{position:relative;width:1200px;height:1000px}

  /* Front of flyer */
  .flyer-front{position:absolute;left:100px;top:190px;width:440px;height:620px;overflow:hidden;
    box-shadow:0 4px 14px rgba(0,0,0,.18)}
  .front-photo{position:absolute;inset:0;
    background:linear-gradient(115deg,var(--crisp) 0%,var(--crisp-light) 38%,var(--chip) 60%,#f6f1e6 100%)}
  .front-band{position:absolute;left:90px;right:0;top:196px;height:120px;background:var(--navy)}
  .front-name{position:absolute;left:0;right:0;top:30px;display:flex;align-items:center;justify-content:center;gap:12px;
    color:var(--red);font-family:"Arimo",sans-serif;font-weight:700;font-size:36px;line-height:1;letter-spacing:1px}
  .name-square{width:18px;height:18px;background:var(--red);flex:none}
  .front-tagline{position:absolute;left:0;right:0;top:74px;text-align:center;color:var(--red);
    font-family:"Arimo",sans-serif;font-weight:700;font-size:22px;line-height:1}
  .front-contact{position:absolute;left:0;right:0;bottom:32px;text-align:center;color:var(--navy);
    font-family:"Open Sans",sans-serif;font-weight:600;font-size:14px;line-height:19px}

  /* Menu side */
  .flyer-menu{position:absolute;left:600px;top:180px;width:500px;height:640px;background:var(--yellow);
    overflow:hidden;box-shadow:0 4px 14px rgba(0,0,0,.18)}
  .menu-corner{position:absolute;left:0;top:0;width:150px;height:40px;background:var(--red)}
  .menu-header{position:absolute;left:150px;top:40px;right:0;height:72px;background:var(--red)}
  .menu-title{position:absolute;left:28px;top:10px;color:var(--white);font-family:"Lora",serif;
    font-style:italic;font-weight:700;font-size:44px;line-height:1}
  .menu-icon{position:absolute;right:22px;top:20px;width:34px;height:34px;border-radius:50%;background:var(--white)}
  .rope-decor{position:absolute;left:0;right:0;bottom:0;height:96px;
    background:linear-gradient(180deg,rgba(255,255,255,0) 0%,rgba(255,255,255,.45) 100%)}

  .side-band{position:absolute;left:48px;top:0;width:104px;height:540px;background:var(--navy)}
  .side-name{position:absolute;left:52px;top:270px;width:460px;transform:translate(-50%,-50%) rotate(-90deg);
    text-align:center;color:var(--red);font-family:"Arimo",sans-serif;font-weight:700;line-height:1;white-space:nowrap}
  .side-name .name{font-size:38px;letter-spacing:1px}
  .side-name .sub{font-size:24px;margin-top:8px}

  .menu-list{position:absolute;left:178px;top:126px;width:300px;font-family:"Arimo",sans-serif;font-weight:700}
  .menu-section{margin-bottom:12px}
  .section-tag{position:relative;display:inline-block;height:20px;width:150px;background:var(--navy);color:var(--white);
    font-size:12px;line-height:20px;padding-left:44px;margin-bottom:6px;
    clip-path:polygon(0 0,100% 0,92% 100%,0 100%)}
  .menu-row{display:grid;grid-template-columns:1fr 56px 56px;font-size:13px;line-height:16px;color:var(--red)}
  .menu-row .price{text-align:right}
  .col-head{color:var(--navy);font-size:12px}
  .drink-name{font-size:13px;line-height:16px;color:var(--red)}
  .drink-list{font-size:10px;line-height:12px;color:var(--red);font-style:italic}
  .row-gap{margin-top:6px}
</style>
</head>
<body>
<main class="canvas">

  <section class="flyer-front">
    <div class="front-photo" role="img" aria-label="Photograph of battered fish with chips, salad and a lemon wedge"></div>
    <div class="front-band">
      <div class="front-name"><span class="name-square"></span>MALLOWBYS</div>
      <div class="front-tagline">Fish &amp; Chips</div>
    </div>
    <div class="front-contact">
      Fish &amp; Chips Takeaway<br>
      17 Fennick Lane, Hollowmere KT4 7RD<br>
      TEL: 0208 6142937
    </div>
  </section>

  <section class="flyer-menu">
    <div class="menu-corner"></div>
    <div class="menu-header">
      <div class="menu-title">menu</div>
      <div class="menu-icon" role="img" aria-label="Small fish icon"></div>
    </div>
    <div class="rope-decor" role="img" aria-label="Pale anchor and rope decoration"></div>

    <div class="side-band">
      <div class="side-name">
        <div class="name">MALLOWBYS</div>
        <div class="sub">Fish &amp; Chips</div>
      </div>
    </div>

    <div class="menu-list">
      <div class="menu-section">
        <div class="section-tag">FISH</div>
        <div class="menu-row col-head"><span></span><span class="price">Small</span><span class="price">Large</span></div>
        <div class="menu-row"><span>Cod</span><span class="price">10.95</span><span class="price">11.95</span></div>
        <div class="menu-row"><span>Plaice</span><span class="price">12.95</span><span class="price">13.95</span></div>
        <div class="menu-row"><span>Haddock</span><span class="price">11.95</span><span class="price">12.95</span></div>
        <div class="menu-row"><span>Scampi &amp; Chips</span><span class="price">14.95</span><span class="price">15.95</span></div>
      </div>
      <div class="menu-section">
        <div class="section-tag">CHIPS</div>
        <div class="menu-row"><span>Chips</span><span class="price">3.00</span><span class="price">4.00</span></div>
        <div class="menu-row"><span>Chips Butty</span><span class="price">3.25</span><span class="price">4.25</span></div>
        <div class="menu-row"><span>Cheese &amp; Chips</span><span class="price">3.75</span><span class="price">4.75</span></div>
        <div class="menu-row"><span>Coleslaw &amp; Chips</span><span class="price">3.75</span><span class="price">4.75</span></div>
        <div class="menu-row"><span>Chips &amp; Gravy</span><span class="price">4.00</span><span class="price">5.00</span></div>
      </div>
      <div class="menu-section">
        <div class="section-tag">EXTRAS</div>
        <div class="menu-row"><span>Chicken Strips</span><span class="price">4.50</span><span class="price">5.50</span></div>
        <div class="menu-row"><span>Fish Cake</span><span class="price">2.00</span><span></span></div>
        <div class="menu-row"><span>Onion Rings</span><span class="price">2.00</span><span></span></div>
        <div class="menu-row"><span>Coleslaw</span><span class="price">1.25</span><span></span></div>
        <div class="menu-row"><span>Buttered Roll</span><span class="price">.50</span><span></span></div>
        <div class="menu-row"><span>Pickled Egg</span><span class="price">.40</span><span></span></div>
        <div class="menu-row"><span>Pickled onion</span><span class="price">.40</span><span></span></div>
      </div>
      <div class="menu-section">
        <div class="section-tag">DRINKS</div>
        <div class="menu-row"><span class="drink-name">Cans</span><span class="price">1.00</span><span></span></div>
        <div class="drink-list">Kola Royale, Fizzo, Lemo Up, Citra Pop<br>Diet Cola, Dr. Spice</div>
        <div class="menu-row row-gap"><span class="drink-name">Bottles</span><span class="price">2.00</span><span></span></div>
        <div class="drink-list">Kola Royale, Fizzo, Citra Pop<br>Diet Cola, Water</div>
      </div>
    </div>
  </section>

</main>
</body>
</html>
```